Lotus Road Journeys - Where Neighbours Build Tomorrow

I am producing a book about humanitarian work done by Australians in Cambodia, mainly house building in poor villages. The images uploaded have been selected to link to the word 'Adventures' which emphasize Australians and Cambodians working together to bring about meaningful change in the lives of the recipients as well as those giving. The book is a coffee table type book with 50% text 50% images, telling of work done over the last 15 years. Cambodians save a little for their house but the majority is donated by Australians who travel there and actually help build the houses. The lives of both are changed in the process. The book will be landscape format. I have two more images which I am unable to upload - I can attach to an email. I have some text to give you for the back cover, a logo for back cover page, which is attached and authors names: Ray Stannard and Doug Whitcombe.
The back cover text is here:
'Approaching retirement, Dean and Helena Tobart decided to use their organisational skills and knowledge in Cambodia to help those less fortunate than themselves own a simple house. They also wanted to empower other West Australians to join them in this work.
Dean and Helena subsequently created a hands-on volunteering experience where people didn’t just give or raise money to help to build these houses but went to Cambodia to complete their construction.
This book tells the powerful stories of some volunteers, including Harbour Side Falcons football players and their mothers, who became involved in this work, the people they helped and how lives were transformed.
Target Market(s)
Australians of any age who might be interested in becoming involved - who want serious (meaningful) fun (doing different things in exotic locations)
Industry/Entity Type
Humanitarian work
Colors
Designer to choose colors to be used in the design.
Requirements
Must have
- The image 'tomdarvo' is of a couple of famous sports people and we would like it to be easily viewed though not dominant
Nice to have
- Young and old volunteers - there is no stereotype
Should not have
- Any negative portrayals of Cambodians - not poor, but joyous. It should not suggest giving but experiencing.

```html
<!DOCTYPE html>
<html lang="en">
<head>
<meta charset="utf-8">
<title>Lotus Road Journeys – Book Cover Spread</title>
<link href="https://fonts.googleapis.com/css2?family=Krona+One&family=Arimo:wght@400&family=Libre+Baskerville&display=swap" rel="stylesheet">
<style>
  :root {
    --sky-light: #eaf3fc;
    --sky: #b4d7f3;
    --lime: #6ad400;
    --lime-soft: rgba(106, 212, 0, 0.9);
    --ink: #0b0b0b;
    --paper-grey: #e4e4e4;
    --photo-grey: #cfcfcf;
    --badge-dark: #222222;
    --badge-text: #f2f2f2;
  }
  html, body {
    margin: 0;
    padding: 0;
    width: 1200px;
    height: 1200px;
    overflow: hidden;
  }
  body {
    position: relative;
    background: radial-gradient(ellipse at center, var(--sky-light) 0%, var(--sky) 75%);
    font-family: "Arimo", Arial, sans-serif;
  }
  .spread {
    position: absolute;
    left: 47px;
    top: 407px;
    width: 1106px;
    height: 387px;
  }

  /* Back cover */
  .back-cover {
    position: absolute;
    left: 0; top: 0;
    width: 534px; height: 387px;
    background: linear-gradient(135deg, #dcdcdc 0%, var(--paper-grey) 50%, #d6d6d6 100%);
  }
  .back-copy {
    position: absolute;
    left: 63px; top: 48px;
    width: 407px;
    color: var(--ink);
    font-size: 7.6px;
    line-height: 13.7px;
    text-align: justify;
  }
  .back-copy p { margin: 0 0 13.7px; text-indent: 23px; }
  .back-rule {
    position: absolute;
    left: 63px; top: 273px;
    width: 407px; height: 2px;
    background: var(--lime);
  }
  .publisher-badge {
    position: absolute;
    left: 63px; top: 302px;
    width: 123px; height: 44px;
    background: var(--badge-dark);
    display: flex;
    align-items: center;
    justify-content: center;
  }
  .publisher-name {
    color: var(--badge-text);
    font-family: "Libre Baskerville", Georgia, serif;
    font-size: 10px;
  }

  /* Spine */
  .spine {
    position: absolute;
    left: 534px; top: 0;
    width: 38px; height: 387px;
    background: var(--lime);
  }
  .spine-text {
    position: absolute;
    left: 0; top: 0;
    width: 387px; height: 38px;
    transform-origin: 0 0;
    transform: translate(38px, 0) rotate(90deg);
    color: var(--ink);
  }
  .spine-title {
    position: absolute;
    left: 20px; top: 3px;
    font-family: "Krona One", sans-serif;
    font-size: 10.5px;
    letter-spacing: 1px;
    white-space: nowrap;
  }
  .spine-subtitle {
    position: absolute;
    left: 20px; top: 20px;
    font-family: "Krona One", sans-serif;
    font-size: 6px;
    white-space: nowrap;
  }
  .spine-authors {
    position: absolute;
    left: 296px; top: 4px;
    width: 85px;
    font-family: "Krona One", sans-serif;
    font-size: 6px;
    line-height: 9.5px;
    text-align: center;
    white-space: nowrap;
  }

  /* Front cover */
  .front-cover {
    position: absolute;
    left: 572px; top: 0;
    width: 534px; height: 387px;
    background: var(--paper-grey);
  }
  .front-backdrop {
    position: absolute;
    left: 0; top: 0;
    width: 534px; height: 387px;
    background: linear-gradient(180deg, #d8d8d8 0%, var(--paper-grey) 60%, #d2d2d2 100%);
  }
  .title-band {
    position: absolute;
    left: 0; top: 0;
    width: 534px; height: 128px;
    background: var(--lime-soft);
  }
  .front-title {
    position: absolute;
    left: 0; top: 33px;
    width: 534px;
    margin: 0;
    text-align: center;
    font-family: "Krona One", sans-serif;
    font-weight: 400;
    font-size: 33px;
    line-height: 38px;
    letter-spacing: 2px;
    color: var(--ink);
  }
  .photo-strip { position: absolute; top: 128px; height: 110px; }
  .photo-team   { left: 0;   width: 165px; background: linear-gradient(160deg, #9cc2e8 0%, #7a5aa8 55%, #6d8a4a 100%); }
  .photo-build  { left: 168px; width: 196px; background: linear-gradient(180deg, #6ea6e6 0%, #cfe2f2 45%, #4c7a52 75%, #9a8a6a 100%); }
  .photo-crowd  { left: 368px; width: 166px; background: linear-gradient(160deg, #a58a72 0%, #5e4a3c 50%, #7b6a5e 100%); }
  .front-subtitle {
    position: absolute;
    left: 0; top: 256px;
    width: 534px;
    margin: 0;
    text-align: center;
    font-family: "Krona One", sans-serif;
    font-weight: 400;
    font-size: 17px;
    line-height: 21px;
    color: var(--ink);
  }
  .author-band {
    position: absolute;
    left: 0; top: 321px;
    width: 534px; height: 35px;
    background: var(--lime-soft);
    display: flex;
    align-items: center;
    justify-content: center;
    font-family: "Krona One", sans-serif;
    font-size: 12px;
    color: var(--ink);
    font-variant: small-caps;
  }
</style>
</head>
<body>
  <div class="spread">
    <section class="back-cover" role="img" aria-label="Faded black-and-white photo of a cheering crowd of villagers and volunteers">
      <div class="back-copy">
        <p>Lorem ipsum dolor sit amet, consectetur adipiscing elit. Sed convallis, massa consectetur aliquet consectetur, purus diam dignissim tortor, malesuada sodales lacus ex non tortor. In scelerisque pharetra maximus. Maecenas mattis tellus est, pretium vehicula lacus feugiat nec. Curabitur quis justo tellus. Integer ut velit nec nulla cursus bibendum id at leo. Cras in tempor lacus. Nulla felis odio, pulvinar et justo eu, pretium dictum risus. Nulla tellus odio, bibendum non tellus et, imperdiet rhoncus nibh. Proin in ornare leo. Aliquam pretium vestibulum libero et egestas. Donec blandit massa quis leo tempor, sed tincidunt risus maximus. Duis sit amet eros at ligula sodales molestie. Sed arcu velit, congue et tellus nec, pulvinar commodo arcu. Sed mollis varius sapien, id finibus neque consectetur vel.</p>
        <p>Nam viverra euismod purus eget tempor. Proin rhoncus metus tincidunt porta pretium. Nullam vestibulum rhoncus velit sit amet molestie. Pellentesque finibus purus quis ornare faucibus. Sed fermentum, erat non varius interdum, nulla turpis rhoncus odio, quis maximus dui ipsum sit amet ipsum. Phasellus suscipit ex est, vitae volutpat orci scelerisque eget. Vestibulum lobortis et purus sed semper. Nulla nec felis at dui vulputate gravida. Suspendisse venenatis velit at tellus ornare, eu venenatis nibh euismod. Phasellus auctor luctus neque eu rutrum. Suspendisse sit amet justo maximus, luctus ipsum sit amet, egestas leo. Sed arcu ante, vehicula ultrices diam in, ultrices cursus turpis. Fusce dictum nec tellus sit amet ultrices. Praesent sem felis, ultricies ac ante id, tincidunt fermentum elit.</p>
      </div>
      <div class="back-rule"></div>
      <div class="publisher-badge"><span class="publisher-name">Riverstone Press</span></div>
    </section>

    <section class="spine">
      <div class="spine-text">
        <div class="spine-title">LOTUS ROAD JOURNEYS</div>
        <div class="spine-subtitle">WHERE NEIGHBOURS BUILD TOMORROW</div>
        <div class="spine-authors">RAY STANNARD<br>&amp;<br>DOUG WHITCOMBE</div>
      </div>
    </section>

    <section class="front-cover">
      <div class="front-backdrop" role="img" aria-label="Faded black-and-white photo of joyful villagers waving"></div>
      <div class="title-band"></div>
      <h1 class="front-title">LOTUS ROAD<br>JOURNEYS</h1>
      <div class="photo-strip photo-team" role="img" aria-label="Photo of four volunteers in purple shirts standing together in a village"></div>
      <div class="photo-strip photo-build" role="img" aria-label="Photo of volunteers building a raised timber house under a blue sky"></div>
      <div class="photo-strip photo-crowd" role="img" aria-label="Photo of a volunteer surrounded by smiling village children"></div>
      <h2 class="front-subtitle">WHERE NEIGHBOURS<br>BUILD TOMORROW</h2>
      <div class="author-band">Ray Stannard &amp; Doug Whitcombe</div>
    </section>
  </div>
</body>
</html>
```